KR TMW PowerPoint Template Design

Looking for an eye catching and clean powerpoint template to deliver sales proposals to our clients. KR TMW is a sales and marketing representation business in the hospitality industry, Logo it attached.

```html
<!DOCTYPE html>
<html lang="en">
<head>
<meta charset="utf-8">
<title>KR TMW Presentation Template</title>
<link href="https://fonts.googleapis.com/css2?family=Open+Sans:wght@400;600;700&display=swap" rel="stylesheet">
<style>
:root{
  --canvas:#a6a6a6;
  --gold:#86703a;
  --gold-dark:#6f5c2e;
  --white:#ffffff;
  --ink:#3a3a3a;
  --muted:#7a7a7a;
  --label:#e4e1da;
}
*{margin:0;padding:0;box-sizing:border-box}
html,body{width:1200px;height:1101px;overflow:hidden;background:var(--canvas);font-family:"Open Sans",Arial,sans-serif}
.deck{position:relative;width:1200px;height:1101px}
.slide{position:absolute;width:242px;height:135px;background:var(--white);overflow:hidden}
.slide>*{position:absolute}
.gold{background:var(--gold)}
.photo{background:linear-gradient(135deg,#5f625f 0%,#9c9a90 55%,#c9c4b5 100%)}
.photo-warm{background:linear-gradient(135deg,#6e5a2b 0%,#9b8757 60%,#c2b48c 100%)}
.photo-sky{background:linear-gradient(180deg,#8fb1cf 0%,#c9d9e6 55%,#6f7e86 100%)}
.photo-city{background:linear-gradient(180deg,#33405a 0%,#c98a4a 60%,#2d2f36 100%)}
.veil{background:rgba(134,112,58,.82)}
.h{font-weight:600;color:var(--gold);font-size:6.5px;letter-spacing:.2px;text-transform:uppercase}
.h-white{color:var(--white)}
.title{font-weight:600;font-size:8px;color:var(--white)}
.tx{font-size:2.7px;line-height:1.4;color:var(--muted)}
.tx-w{color:#f1ead9}
.sub{font-size:3.4px;font-weight:600;color:var(--gold)}
.sub-w{color:var(--white)}
.quote{font-weight:600;color:var(--white);text-align:center;line-height:1.35}
.quote-g{color:var(--gold)}
.item{width:60px}
.item svg{display:block;width:11px;height:9px;margin-bottom:2px}
.circle{border-radius:50%}
.pill{background:var(--gold);color:var(--white);font-size:2.8px;font-weight:600;padding:1px 3px;display:inline-block}
.card{background:var(--gold);text-align:center;color:var(--white)}
.footer{font-size:2.3px;color:var(--gold)}
</style>
</head>
<body>
<div class="deck">

<!-- Row 1 -->
<section class="slide slide-cover" style="left:70px;top:72px">
  <div class="photo-warm" role="img" aria-label="Photo of hands working with financial charts, gold toned" style="inset:0"></div>
  <div style="right:12px;top:12px;font-size:7px;font-weight:700;color:var(--white)">KR TMW</div>
  <div style="left:33px;top:45px;width:120px;font-size:9.5px;line-height:1.1;color:var(--white);font-weight:600">Lorem ipsum dolor sit amet, consectetur adipiscing elit, sed do eiusmod tempor</div>
</section>

<section class="slide slide-intro" style="left:344px;top:72px">
  <div class="photo" role="img" aria-label="Photo of two colleagues reviewing documents in an office" style="left:0;top:0;width:121px;height:135px"></div>
  <div class="gold" style="left:121px;top:0;width:121px;height:135px"></div>
  <div class="title" style="left:142px;top:31px">Introduction</div>
  <p class="tx tx-w" style="left:142px;top:48px;width:86px">Lorem ipsum dolor sit amet, consectetur adipiscing elit, sed do eiusmod tempor incididunt ut labore et dolore magna aliqua. Ut enim ad minim veniam, quis nostrud exercitation ullamco laboris nisi ut aliquip ex ea commodo consequat. Duis aute irure dolor in reprehenderit in voluptate velit esse cillum dolore eu fugiat nulla pariatur.</p>
</section>

<section class="slide slide-about" style="left:616px;top:72px">
  <div class="photo-sky" role="img" aria-label="Photo of modern glass office buildings and trees" style="inset:0"></div>
  <div style="left:20px;top:0;width:94px;height:113px;background:var(--white)"></div>
  <div class="title" style="left:34px;top:18px;color:var(--gold)">About Us</div>
  <p class="tx" style="left:34px;top:33px;width:74px">Lorem ipsum dolor sit amet, consectetur adipiscing elit, sed do eiusmod tempor incididunt ut labore et dolore magna aliqua. Ut enim ad minim veniam, quis nostrud exercitation ullamco laboris nisi ut aliquip ex ea commodo consequat. Duis aute irure dolor in reprehenderit.</p>
</section>

<section class="slide slide-features" style="left:887px;top:72px">
  <div class="photo-sky" role="img" aria-label="Photo of a stock market display board" style="left:92px;top:0;width:150px;height:135px"></div>
  <div class="gold" style="left:0;top:0;width:92px;height:135px"></div>
  <div class="sub sub-w" style="left:17px;top:28px;font-size:5px">Lorem Ipsum</div>
  <p class="tx tx-w" style="left:17px;top:38px;width:52px">Lorem ipsum dolor sit amet, consectetur adipiscing elit, sed do eiusmod tempor incididunt ut labore et dolore magna aliqua. Ut enim ad minim veniam, quis nostrud exercitation.</p>
  <div style="left:70px;top:23px;width:152px;height:93px;background:var(--white)"></div>
  <div class="item" style="left:89px;top:35px"><svg viewBox="0 0 11 9"><rect x="1" y="1" width="9" height="7" fill="none" stroke="#86703a" stroke-width=".8"/></svg><div class="sub">Lorem Ipsum</div><p class="tx">Lorem ipsum dolor sit amet</p></div>
  <div class="item" style="left:158px;top:35px"><svg viewBox="0 0 11 9"><path d="M2 8V4M5 8V2M8 8V5" stroke="#86703a" stroke-width="1"/></svg><div class="sub">Lorem Ipsum</div><p class="tx">Lorem ipsum dolor sit amet</p></div>
  <div class="item" style="left:89px;top:75px"><svg viewBox="0 0 11 9"><circle cx="5.5" cy="5" r="3.5" fill="#86703a"/></svg><div class="sub">Lorem Ipsum</div><p class="tx">Lorem ipsum dolor sit amet</p></div>
  <div class="item" style="left:158px;top:75px"><svg viewBox="0 0 11 9"><rect x="3" y="4" width="5" height="4.5" fill="#86703a"/><path d="M4 4V2.5a1.5 1.5 0 013 0V4" fill="none" stroke="#86703a" stroke-width=".8"/></svg><div class="sub">Lorem Ipsum</div><p class="tx">Lorem ipsum dolor sit amet</p></div>
</section>

<!-- Row 2 -->
<section class="slide slide-team" style="left:70px;top:236px">
  <div class="h" style="left:14px;top:8px">Meet our team</div>
  <div class="photo" role="img" aria-label="Portrait photo of team member" style="left:14px;top:28px;width:32px;height:72px"></div>
  <div class="photo" role="img" aria-label="Portrait photo of team member" style="left:51px;top:28px;width:32px;height:72px"></div>
  <div class="photo" role="img" aria-label="Portrait photo of team member" style="left:88px;top:28px;width:32px;height:72px"></div>
  <div class="photo" role="img" aria-label="Portrait photo of team member" style="left:125px;top:28px;width:32px;height:72px"></div>
  <div class="photo" role="img" aria-label="Portrait photo of team member" style="left:162px;top:28px;width:32px;height:72px"></div>
  <div class="photo" role="img" aria-label="Portrait photo of team member" style="left:199px;top:28px;width:32px;height:72px"></div>
  <div class="tx" style="left:14px;top:102px;width:32px;height:12px;background:var(--label);text-align:center;padding-top:1px"><b style="color:var(--gold)">Owen Hale</b><br>CEO/President</div>
  <div class="tx" style="left:51px;top:102px;width:32px;height:12px;background:var(--label);text-align:center;padding-top:1px"><b style="color:var(--gold)">Nora Pike</b><br>VP-Finance</div>
  <div class="tx" style="left:88px;top:102px;width:32px;height:12px;background:var(--label);text-align:center;padding-top:1px"><b style="color:var(--gold)">Ivy Marsh</b><br>Human Resource</div>
  <div class="tx" style="left:125px;top:102px;width:32px;height:12px;background:var(--label);text-align:center;padding-top:1px"><b style="color:var(--gold)">Clara Dunn</b><br>Managing Director</div>
  <div class="tx" style="left:162px;top:102px;width:32px;height:12px;background:var(--label);text-align:center;padding-top:1px"><b style="color:var(--gold)">Felix Grant</b><br>Manager-Delivery</div>
  <div class="tx" style="left:199px;top:102px;width:32px;height:12px;background:var(--label);text-align:center;padding-top:1px"><b style="color:var(--gold)">Maya Stone</b><br>Manager-Accounts</div>
</section>

<section class="slide slide-services" style="left:344px;top:236px">
  <div class="h" style="left:14px;top:8px">Our services</div>
  <div class="item" style="left:14px;top:33px"><svg viewBox="0 0 11 9"><rect x="1" y="1" width="9" height="6" fill="none" stroke="#86703a" stroke-width=".8"/></svg></div>
  <div style="left:36px;top:33px;width:45px"><div class="sub" style="font-size:2.8px">Lorem ipsum dolor</div><p class="tx">Lorem ipsum dolor sit amet, consectetur</p></div>
  <div class="item" style="left:86px;top:33px"><svg viewBox="0 0 11 9"><rect x="1" y="1" width="9" height="7" fill="none" stroke="#86703a" stroke-width=".8"/></svg></div>
  <div style="left:108px;top:33px;width:45px"><div class="sub" style="font-size:2.8px">Lorem ipsum dolor</div><p class="tx">Lorem ipsum dolor sit amet, consectetur</p></div>
  <div class="item" style="left:14px;top:66px"><svg viewBox="0 0 11 9"><path d="M1 8h9M3 8V3h5v5" fill="none" stroke="#86703a" stroke-width=".8"/></svg></div>
  <div style="left:36px;top:66px;width:45px"><div class="sub" style="font-size:2.8px">Lorem ipsum dolor</div><p class="tx">Lorem ipsum dolor sit amet, consectetur</p></div>
  <div class="item" style="left:86px;top:66px"><svg viewBox="0 0 11 9"><path d="M2 8V5M5 8V3M8 8V1" stroke="#86703a" stroke-width="1"/></svg></div>
  <div style="left:108px;top:66px;width:45px"><div class="sub" style="font-size:2.8px">Lorem ipsum dolor</div><p class="tx">Lorem ipsum dolor sit amet, consectetur</p></div>
  <div class="item" style="left:14px;top:99px"><svg viewBox="0 0 11 9"><rect x="2" y="1" width="7" height="7" fill="none" stroke="#86703a" stroke-width=".8"/></svg></div>
  <div style="left:36px;top:99px;width:45px"><div class="sub" style="font-size:2.8px">Lorem ipsum dolor</div><p class="tx">Lorem ipsum dolor sit amet, consectetur</p></div>
  <div class="item" style="left:86px;top:99px"><svg viewBox="0 0 11 9"><circle cx="5.5" cy="2.5" r="1.5" fill="none" stroke="#86703a" stroke-width=".7"/><circle cx="2.5" cy="7" r="1.5" fill="none" stroke="#86703a" stroke-width=".7"/><circle cx="8.5" cy="7" r="1.5" fill="none" stroke="#86703a" stroke-width=".7"/></svg></div>
  <div style="left:108px;top:99px;width:45px"><div class="sub" style="font-size:2.8px">Lorem ipsum dolor</div><p class="tx">Lorem ipsum dolor sit amet, consectetur</p></div>
  <div class="photo" role="img" aria-label="Photo of a smiling woman with glasses using a laptop" style="left:161px;top:12px;width:73px;height:112px"></div>
</section>

<section class="slide slide-testimonials" style="left:616px;top:236px">
  <div class="gold" style="left:0;top:0;width:100px;height:135px"></div>
  <div style="left:40px;top:22px;font-size:22px;font-weight:700;color:var(--white);line-height:1">&ldquo;</div>
  <p class="quote" style="left:18px;top:48px;width:64px;font-size:4.6px">&ldquo;Lorem ipsum dolor sit amet, consectetur adipiscing elit. Phasellus sodales, ligula ultrices tempus ristique, tellus justo aliquam dui, nec Lorem ipsum dolor sit amet, consectetur</p>
  <div class="h" style="left:113px;top:11px">Testimonials</div>
  <div class="photo circle" role="img" aria-label="Client portrait" style="left:113px;top:32px;width:22px;height:22px"></div>
  <div style="left:142px;top:33px;width:88px"><div class="sub">Lorem ipsum</div><p class="tx">Lorem ipsum dolor sit amet, consectetur adipiscing elit, sed do eiusmod tempor incididunt ut labore et dolore magna aliqua.</p></div>
  <div class="photo circle" role="img" aria-label="Client portrait" style="left:113px;top:66px;width:22px;height:22px"></div>
  <div style="left:142px;top:67px;width:88px"><div class="sub">Lorem ipsum</div><p class="tx">Lorem ipsum dolor sit amet, consectetur adipiscing elit, sed do eiusmod tempor incididunt ut labore et dolore magna aliqua.</p></div>
  <div class="photo circle" role="img" aria-label="Client portrait" style="left:113px;top:100px;width:22px;height:22px"></div>
  <div style="left:142px;top:101px;width:88px"><div class="sub">Lorem ipsum</div><p class="tx">Lorem ipsum dolor sit amet, consectetur adipiscing elit, sed do eiusmod tempor incididunt ut labore et dolore magna aliqua.</p></div>
</section>

<section class="slide slide-portfolio" style="left:887px;top:236px">
  <div class="photo" role="img" aria-label="Photo of an office workstation with monitors" style="left:0;top:0;width:110px;height:135px"></div>
  <div class="h" style="left:151px;top:12px">Our portfolio</div>
  <div class="item" style="left:126px;top:34px"><svg viewBox="0 0 11 9"><rect x="1" y="1" width="9" height="7" fill="none" stroke="#86703a" stroke-width=".8"/></svg></div>
  <div style="left:152px;top:33px;width:80px"><div class="sub">Lorem ipsum</div><p class="tx">Lorem ipsum dolor sit amet, consectetur adipiscing elit, sed do eiusmod tempor incididunt ut labore.</p></div>
  <div class="item" style="left:126px;top:69px"><svg viewBox="0 0 11 9"><rect x="1" y="1" width="9" height="7" fill="none" stroke="#86703a" stroke-width=".8"/><path d="M1 3h9" stroke="#86703a" stroke-width=".8"/></svg></div>
  <div style="left:152px;top:68px;width:80px"><div class="sub">Lorem ipsum</div><p class="tx">Lorem ipsum dolor sit amet, consectetur adipiscing elit, sed do eiusmod tempor incididunt ut labore.</p></div>
  <div class="item" style="left:126px;top:104px"><svg viewBox="0 0 11 9"><rect x="2" y="1" width="7" height="7" fill="none" stroke="#86703a" stroke-width=".8"/></svg></div>
  <div style="left:152px;top:103px;width:80px"><div class="sub">Lorem ipsum</div><p class="tx">Lorem ipsum dolor sit amet, consectetur adipiscing elit, sed do eiusmod tempor incididunt ut labore.</p></div>
</section>

<!-- Row 3 -->
<section class="slide slide-quote-band" style="left:70px;top:399px">
  <div class="photo-warm" role="img" aria-label="Photo of an empty boardroom, gold toned" style="left:0;top:0;width:242px;height:64px"></div>
  <p class="quote" style="left:20px;top:24px;width:202px;font-size:5px">&ldquo;Lorem ipsum dolor sit amet, consectetur adipiscing elit. Phasellus sodales, ligula ultrices tempus ristique, tellus justo aliquam dui,</p>
  <div style="left:32px;top:74px;width:50px;text-align:center"><svg viewBox="0 0 11 9" style="width:14px;height:12px"><rect x="1" y="1" width="9" height="7" fill="none" stroke="#86703a" stroke-width=".8"/><path d="M2 6l2-2 2 1 3-3" fill="none" stroke="#86703a" stroke-width=".6"/></svg><div class="sub">Lorem ipsum</div><p class="tx">Lorem ipsum dolor sit amet, consectetur adipiscing elit</p></div>
  <div style="left:96px;top:74px;width:50px;text-align:center"><svg viewBox="0 0 11 9" style="width:14px;height:12px"><rect x="1" y="1" width="9" height="7" fill="none" stroke="#86703a" stroke-width=".8"/><path d="M3 7V4M5.5 7V2M8 7V5" stroke="#86703a" stroke-width=".8"/></svg><div class="sub">Lorem ipsum</div><p class="tx">Lorem ipsum dolor sit amet, consectetur adipiscing elit</p></div>
  <div style="left:160px;top:74px;width:50px;text-align:center"><svg viewBox="0 0 11 9" style="width:14px;height:12px"><rect x="2" y="1" width="7" height="7" fill="none" stroke="#86703a" stroke-width=".8"/><path d="M3.5 3h4M3.5 5h4" stroke="#86703a" stroke-width=".6"/></svg><div class="sub">Lorem ipsum</div><p class="tx">Lorem ipsum dolor sit amet, consectetur adipiscing elit</p></div>
  <div class="footer" style="left:10px;top:127px">Edit title here</div>
</section>

<section class="slide slide-collage" style="left:344px;top:399px">
  <div class="photo" role="img" aria-label="Collage of business meeting photos" style="left:0;top:0;width:140px;height:135px"></div>
  <div class="title" style="left:166px;top:18px;color:var(--gold)">Lorem Ipsum</div>
  <p class="tx" style="left:156px;top:34px;width:78px;text-align:center;color:var(--ink)">Lorem ipsum dolor sit amet, consectetur adipiscing elit, sed do eiusmod tempor incididunt ut labore et dolore magna aliqua. Ut enim ad minim veniam, quis nostrud exercitation ullamco laboris nisi ut aliquip ex ea commodo consequat. Duis aute irure dolor in reprehenderit in voluptate velit esse cillum dolore eu fugiat nulla pariatur. Excepteur sint occaecat cupidatat non proident, sunt in culpa qui officia deserunt mollit anim id est laborum.</p>
</section>

<section class="slide slide-team-circles" style="left:616px;top:399px">
  <div class="h" style="left:0;top:12px;width:242px;text-align:center">Our team</div>
  <div class="photo circle" role="img" aria-label="Team member portrait" style="left:20px;top:34px;width:36px;height:36px"></div>
  <div style="left:62px;top:36px;width:50px"><span class="pill">Lorem Ipsum</span><p class="tx" style="margin-top:3px">Lorem ipsum dolor sit amet, consectetur adipiscing elit, sed do eiusmod tempor.</p></div>
  <div class="photo circle" role="img" aria-label="Team member portrait" style="left:133px;top:34px;width:36px;height:36px"></div>
  <div style="left:174px;top:36px;width:50px"><span class="pill">Lorem Ipsum</span><p class="tx" style="margin-top:3px">Lorem ipsum dolor sit amet, consectetur adipiscing elit, sed do eiusmod tempor.</p></div>
  <div class="photo circle" role="img" aria-label="Team member portrait" style="left:20px;top:80px;width:36px;height:36px"></div>
  <div style="left:62px;top:82px;width:50px"><span class="pill">Lorem Ipsum</span><p class="tx" style="margin-top:3px">Lorem ipsum dolor sit amet, consectetur adipiscing elit, sed do eiusmod tempor.</p></div>
  <div class="photo circle" role="img" aria-label="Team member portrait" style="left:133px;top:80px;width:36px;height:36px"></div>
  <div style="left:174px;top:82px;width:50px"><span class="pill">Lorem Ipsum</span><p class="tx" style="margin-top:3px">Lorem ipsum dolor sit amet, consectetur adipiscing elit, sed do eiusmod tempor.</p></div>
</section>

<section class="slide slide-quote-split" style="left:887px;top:399px">
  <div class="photo" role="img" aria-label="Photo of a team meeting around a table" style="left:16px;top:0;width:212px;height:63px"></div>
  <p class="quote quote-g" style="left:14px;top:88px;width:68px;font-size:5px;font-weight:400">&ldquo;Lorem ipsum dolor sit amet, consectetur</p>
  <p class="tx" style="left:88px;top:76px;width:140px;color:var(--ink)">&ldquo;Lorem ipsum dolor sit amet, consectetur adipiscing elit. Phasellus sodales, ligula ultrices tempus ristique, tellus justo aliquam dui, nec Lorem ipsum dolor sit amet, consectetur adipiscing elit. Phasellus sodales, ligula ultrices tempus ristique, tellus justo aliquam dui, nec Lorem ipsum dolor sit amet, consectetur adipiscing elit. Phasellus sodales, ligula ultrices tempus ristique, tellus justo aliquam.</p>
</section>

<!-- Row 4 -->
<section class="slide slide-section" style="left:70px;top:563px">
  <div class="photo" role="img" aria-label="Photo of a laptop keyboard and tablet on a desk" style="inset:0"></div>
  <div class="gold" style="left:0;top:30px;width:242px;height:76px;opacity:.95"></div>
  <div style="left:0;top:61px;width:242px;text-align:center;font-size:11.5px;font-weight:600;color:var(--white)">SECTION TITLE HERE</div>
</section>

<section class="slide slide-three-col" style="left:344px;top:563px">
  <div class="photo-warm" role="img" aria-label="Photo of a city street, gold toned" style="left:84px;top:0;width:75px;height:135px"></div>
  <p class="quote" style="left:94px;top:27px;width:55px;font-size:5px;font-weight:400">&ldquo;Lorem ipsum dolor sit amet, consectetur adipiscing elit. Phasellus sodales, ligula ultrices tempus ristique, tellus justo aliquam dui,</p>
  <div style="left:20px;top:26px;width:56px;text-align:right"><span class="pill">Lorem Ipsum</span><p class="tx" style="margin-top:3px">Lorem ipsum dolor sit amet, consectetur adipiscing elit, sed do eiusmod tempor incididunt ut labore et dolore.</p></div>
  <div style="left:20px;top:82px;width:56px;text-align:right"><span class="pill">Lorem Ipsum</span><p class="tx" style="margin-top:3px">Lorem ipsum dolor sit amet, consectetur adipiscing elit, sed do eiusmod tempor incididunt ut labore et dolore.</p></div>
  <div style="left:174px;top:26px;width:56px"><span class="pill">Lorem Ipsum</span><p class="tx" style="margin-top:3px">Lorem ipsum dolor sit amet, consectetur adipiscing elit, sed do eiusmod tempor incididunt ut labore et dolore.</p></div>
  <div style="left:174px;top:82px;width:56px"><span class="pill">Lorem Ipsum</span><p class="tx" style="margin-top:3px">Lorem ipsum dolor sit amet, consectetur adipiscing elit, sed do eiusmod tempor incididunt ut labore et dolore.</p></div>
</section>

<section class="slide slide-team-cards" style="left:616px;top:563px">
  <div class="h" style="left:0;top:12px;width:242px;text-align:center">Our team</div>
  <div class="photo" role="img" aria-label="Photo of a desk with laptops seen from above" style="left:0;top:28px;width:242px;height:80px"></div>
  <div class="card" style="left:22px;top:56px;width:62px;height:40px"><svg viewBox="0 0 11 9" style="width:14px;height:12px;margin-top:8px"><path d="M2 8V5M5 8V2M8 8V4" stroke="#fff" stroke-width="1.6"/></svg><div style="font-size:3.2px;font-weight:600;margin-top:4px">Lorem Ipsum Dolor</div></div>
  <div class="card" style="left:90px;top:56px;width:62px;height:40px"><svg viewBox="0 0 11 9" style="width:14px;height:12px;margin-top:8px"><rect x="2" y="2" width="7" height="6" fill="none" stroke="#fff" stroke-width="1"/><path d="M4 4h3M4 6h3" stroke="#fff" stroke-width=".6"/></svg><div style="font-size:3.2px;font-weight:600;margin-top:4px">Lorem Ipsum Dolor</div></div>
  <div class="card" style="left:158px;top:56px;width:62px;height:40px"><svg viewBox="0 0 11 9" style="width:14px;height:12px;margin-top:8px"><circle cx="3" cy="3" r="1.4" fill="#fff"/><circle cx="8" cy="3" r="1.4" fill="#fff"/><circle cx="5.5" cy="5" r="1.4" fill="#fff"/><path d="M1 8.5h9" stroke="#fff" stroke-width="1.2"/></svg><div style="font-size:3.2px;font-weight:600;margin-top:4px">Lorem Ipsum Dolor</div></div>
  <p class="tx" style="left:22px;top:108px;width:62px;text-align:center">Lorem ipsum dolor sit amet, consectetur adipiscing elit, sed do</p>
  <p class="tx" style="left:90px;top:108px;width:62px;text-align:center">Lorem ipsum dolor sit amet, consectetur adipiscing elit, sed do</p>
  <p class="tx" style="left:158px;top:108px;width:62px;text-align:center">Lorem ipsum dolor sit amet, consectetur adipiscing elit, sed do</p>
  <div class="footer" style="left:10px;top:127px">Edit title here</div>
</section>

<section class="slide slide-quote-photo" style="left:887px;top:563px">
  <p class="quote quote-g" style="left:6px;top:40px;width:56px;font-size:5.4px;font-weight:400">&ldquo;Lorem ipsum dolor sit amet, consectetur adipiscing elit.</p>
  <div class="photo" role="img" aria-label="Photo of a smiling woman working at a laptop" style="left:61px;top:0;width:92px;height:135px"></div>
  <div class="item" style="left:165px;top:17px"><svg viewBox="0 0 11 9"><rect x="3" y="4" width="5" height="4.5" fill="#86703a"/><path d="M4 4V2.5a1.5 1.5 0 013 0V4" fill="none" stroke="#86703a" stroke-width=".8"/></svg></div>
  <div style="left:181px;top:16px;width:52px"><div class="sub" style="font-size:2.9px">Lorem Ipsum Dolor</div><p class="tx">Lorem ipsum dolor sit amet, consectetur adipiscing elit, sed do eiusmod tempor.</p></div>
  <div class="item" style="left:165px;top:57px"><svg viewBox="0 0 11 9"><path d="M1 5l3-3 3 3 3-3" fill="none" stroke="#86703a" stroke-width="1.2"/></svg></div>
  <div style="left:181px;top:56px;width:52px"><div class="sub" style="font-size:2.9px">Lorem Ipsum Dolor</div><p class="tx">Lorem ipsum dolor sit amet, consectetur adipiscing elit, sed do eiusmod tempor.</p></div>
  <div class="item" style="left:165px;top:97px"><svg viewBox="0 0 11 9"><path d="M1 4l4.5-2 4.5 2-4.5 2z" fill="#86703a"/></svg></div>
  <div style="left:181px;top:96px;width:52px"><div class="sub" style="font-size:2.9px">Lorem Ipsum Dolor</div><p class="tx">Lorem ipsum dolor sit amet, consectetur adipiscing elit, sed do eiusmod tempor.</p></div>
</section>

<!-- Row 5 -->
<section class="slide slide-tablet" style="left:70px;top:726px">
  <p class="quote quote-g" style="left:6px;top:40px;width:44px;font-size:5.4px;font-weight:400">&ldquo;Lorem ipsum dolor sit amet, consectetur adipiscing</p>
  <div class="gold" style="left:55px;top:0;width:76px;height:135px"></div>
  <div class="photo" role="img" aria-label="Photo of hands using a tablet" style="left:131px;top:0;width:111px;height:135px"></div>
  <div style="left:69px;top:15px;width:50px"><div class="sub sub-w" style="font-size:3px">Lorem Ipsum Dolor</div><p class="tx tx-w">Lorem ipsum dolor sit amet, consectetur adipiscing elit, sed do eiusmod tempor.</p></div>
  <div style="left:69px;top:55px;width:50px"><div class="sub sub-w" style="font-size:3px">Lorem Ipsum Dolor</div><p class="tx tx-w">Lorem ipsum dolor sit amet, consectetur adipiscing elit, sed do eiusmod tempor.</p></div>
  <div style="left:69px;top:95px;width:50px"><div class="sub sub-w" style="font-size:3px">Lorem Ipsum Dolor</div><p class="tx tx-w">Lorem ipsum dolor sit amet, consectetur adipiscing elit, sed do eiusmod tempor.</p></div>
</section>

<section class="slide slide-split-list" style="left:344px;top:726px">
  <div class="gold" style="left:0;top:0;width:126px;height:135px"></div>
  <div style="left:16px;top:18px;width:100px;font-size:7px;font-weight:600;color:var(--white);line-height:1.3">Lorem ipsum dolor<br>sit amet, consectetur</div>
  <p class="tx tx-w" style="left:16px;top:45px;width:96px">&ldquo;Lorem ipsum dolor sit amet, consectetur adipiscing elit. Phasellus sodales, ligula ultrices tempus ristique, tellus justo aliquam dui, nec Lorem ipsum dolor sit amet, consectetur adipiscing elit. Phasellus sodales, ligula ultrices tempus ristique, tellus justo aliquam dui, nec Lorem ipsum dolor sit amet, consectetur adipiscing elit. Phasellus sodales, ligula ultrices tempus ristique, tellus justo aliquam dui, nec Lorem ipsum dolor sit amet.</p>
  <div class="item" style="left:141px;top:19px"><svg viewBox="0 0 11 9"><circle cx="3" cy="3" r="1.5" fill="#86703a"/><circle cx="8" cy="3" r="1.5" fill="#86703a"/><circle cx="5.5" cy="6" r="1.8" fill="#86703a"/></svg></div>
  <div style="left:164px;top:18px;width:68px"><div class="sub">Lorem ipsum</div><p class="tx">Lorem ipsum dolor sit amet, consectetur adipiscing elit, sed do eiusmod tempor.</p></div>
  <div class="item" style="left:141px;top:59px"><svg viewBox="0 0 11 9"><rect x="1" y="2" width="6" height="4" fill="#86703a"/><rect x="7" y="3.5" width="3" height="2.5" fill="#86703a"/></svg></div>
  <div style="left:164px;top:58px;width:68px"><div class="sub">Lorem ipsum</div><p class="tx">Lorem ipsum dolor sit amet, consectetur adipiscing elit, sed do eiusmod tempor.</p></div>
  <div class="item" style="left:141px;top:99px"><svg viewBox="0 0 11 9"><rect x="1" y="1" width="9" height="7" fill="none" stroke="#86703a" stroke-width=".8"/><path d="M4.5 3v3l2.5-1.5z" fill="#86703a"/></svg></div>
  <div style="left:164px;top:98px;width:68px"><div class="sub">Lorem ipsum</div><p class="tx">Lorem ipsum dolor sit amet, consectetur adipiscing elit, sed do eiusmod tempor.</p></div>
</section>

<section class="slide slide-photo-cards" style="left:616px;top:726px">
  <div class="h" style="left:14px;top:12px">Edit title here</div>
  <div class="card photo-warm" role="img" aria-label="Gold toned office photo behind card" style="left:17px;top:30px;width:66px;height:92px"></div>
  <div class="card photo-warm" role="img" aria-label="Gold toned office photo behind card" style="left:88px;top:30px;width:66px;height:92px"></div>
  <div class="card photo-warm" role="img" aria-label="Gold toned office photo behind card" style="left:159px;top:30px;width:66px;height:92px"></div>
  <div style="left:17px;top:52px;width:66px;text-align:center;color:var(--white)"><svg viewBox="0 0 11 9" style="width:14px;height:12px"><rect x="2" y="2" width="7" height="6" fill="#fff"/></svg><div style="font-size:3.2px;font-weight:600;margin-top:3px">LOREM IPSUM DOLOR</div><p class="tx tx-w" style="width:48px;margin:2px auto 0">&ldquo;Lorem ipsum dolor sit amet, consectetur adipiscing elit.</p></div>
  <div style="left:88px;top:52px;width:66px;text-align:center;color:var(--white)"><svg viewBox="0 0 11 9" style="width:14px;height:12px"><rect x="1.5" y="1.5" width="8" height="6" fill="none" stroke="#fff" stroke-width=".9"/><path d="M3.5 6V4.5M5.5 6V3M7.5 6V4" stroke="#fff" stroke-width=".8"/></svg><div style="font-size:3.2px;font-weight:600;margin-top:3px">LOREM IPSUM DOLOR</div><p class="tx tx-w" style="width:48px;margin:2px auto 0">&ldquo;Lorem ipsum dolor sit amet, consectetur adipiscing elit.</p></div>
  <div style="left:159px;top:52px;width:66px;text-align:center;color:var(--white)"><svg viewBox="0 0 11 9" style="width:14px;height:12px"><path d="M2 5l3.5 3L9 5M5.5 1v6" fill="none" stroke="#fff" stroke-width="1.1"/></svg><div style="font-size:3.2px;font-weight:600;margin-top:3px">LOREM IPSUM DOLOR</div><p class="tx tx-w" style="width:48px;margin:2px auto 0">&ldquo;Lorem ipsum dolor sit amet, consectetur adipiscing elit.</p></div>
</section>

<section class="slide slide-collage-text" style="left:887px;top:726px">
  <div class="photo" role="img" aria-label="Collage of teamwork photos" style="left:12px;top:12px;width:86px;height:112px"></div>
  <div style="left:122px;top:22px;width:110px;font-size:6.5px;color:var(--gold);line-height:1.3">Lorem ipsum dolor<br>sit amet, consectetur</div>
  <p class="tx" style="left:122px;top:47px;width:106px;color:var(--ink)">&ldquo;Lorem ipsum dolor sit amet, consectetur adipiscing elit. Phasellus sodales, ligula ultrices tempus ristique, tellus justo aliquam dui, nec Lorem ipsum dolor sit amet, consectetur adipiscing elit. Phasellus sodales, ligula ultrices tempus ristique, tellus justo aliquam dui, nec Lorem ipsum dolor sit amet, consectetur adipiscing elit. Phasellus sodales, ligula ultrices tempus ristique, tellus justo aliquam dui, nec Lorem ipsum dolor sit amet.</p>
</section>

<!-- Row 6 -->
<section class="slide slide-city" style="left:70px;top:893px">
  <div class="h" style="left:14px;top:12px">Edit title here</div>
  <div class="photo-city" role="img" aria-label="Photo of a city skyline at dusk with highway light trails" style="left:15px;top:28px;width:212px;height:63px"></div>
  <div class="item" style="left:20px;top:101px"><svg viewBox="0 0 11 9"><circle cx="3" cy="3" r="1.5" fill="#86703a"/><circle cx="8" cy="3" r="1.5" fill="#86703a"/><circle cx="5.5" cy="6" r="1.8" fill="#86703a"/></svg></div>
  <div style="left:39px;top:100px;width:72px"><div class="sub">Lorem ipsum</div><p class="tx">Lorem ipsum dolor sit amet, consectetur adipiscing elit, sed do eiusmod tempor incididunt.</p></div>
  <div class="item" style="left:128px;top:101px"><svg viewBox="0 0 11 9"><rect x="1" y="1" width="9" height="7" fill="none" stroke="#86703a" stroke-width=".8"/><path d="M4.5 3v3l2.5-1.5z" fill="#86703a"/></svg></div>
  <div style="left:148px;top:100px;width:72px"><div class="sub">Lorem ipsum</div><p class="tx">Lorem ipsum dolor sit amet, consectetur adipiscing elit, sed do eiusmod tempor incididunt.</p></div>
</section>

<section class="slide slide-band" style="left:344px;top:893px">
  <div class="gold" style="left:0;top:0;width:242px;height:52px"></div>
  <div class="h h-white" style="left:14px;top:12px">Edit title here</div>
  <p class="tx tx-w" style="left:14px;top:25px;width:124px">&ldquo;Lorem ipsum dolor sit amet, consectetur adipiscing elit. Phasellus sodales, ligula ultrices tempus ristique, tellus justo aliquam dui, nec Lorem ipsum dolor sit amet.</p>
  <div class="photo-sky" role="img" aria-label="Photo of a harbour city skyline with a tall tower" style="left:143px;top:20px;width:83px;height:97px"></div>
  <div style="left:14px;top:63px;font-size:4px;font-weight:600;color:var(--ink)">Lorem ipsum dolor sit amet</div>
  <p class="tx" style="left:14px;top:71px;width:122px;color:var(--ink)">&ldquo;Lorem ipsum dolor sit amet, consectetur adipiscing elit. Phasellus sodales, ligula ultrices tempus ristique, tellus justo aliquam dui, nec Lorem ipsum dolor sit amet, consectetur adipiscing elit. Phasellus sodales, ligula ultrices tempus ristique, tellus justo aliquam dui, nec Lorem ipsum dolor sit amet, consectetur adipiscing elit. Phasellus sodales, ligula ultrices tempus.</p>
  <div class="footer" style="left:10px;top:127px">Edit title here</div>
</section>

<section class="slide slide-desk" style="left:616px;top:893px">
  <div class="photo" role="img" aria-label="Photo of a desk with laptop and documents seen from above" style="left:128px;top:0;width:114px;height:135px"></div>
  <div class="gold" style="left:0;top:0;width:128px;height:135px"></div>
  <div style="left:16px;top:30px;font-size:7px;font-weight:600;color:var(--white)">Lorem ipsum dolor sit</div>
  <p class="tx tx-w" style="left:16px;top:45px;width:100px">Lorem ipsum dolor sit amet, consectetur adipiscing elit. Phasellus sodales, ligula ultrices tempus ristique, tellus justo aliquam dui, nec Lorem ipsum dolor sit amet, consectetur adipiscing elit. Phasellus sodales, ligula ultrices tempus ristique, tellus justo aliquam dui, nec Lorem ipsum dolor sit amet, consectetur adipiscing elit. Phasellus sodales, ligula ultrices tempus ristique, tellus justo aliquam dui.</p>
</section>

<section class="slide slide-thanks" style="left:887px;top:893px">
  <div class="photo-warm" role="img" aria-label="Faint gold toned office photo" style="inset:0;opacity:.35"></div>
  <div class="gold" style="inset:0;opacity:.85"></div>
  <div style="left:56px;top:40px;width:130px;height:1px;background:#d8ccb0"></div>
  <div style="left:0;top:44px;width:242px;text-align:center;font-size:17px;color:var(--white);letter-spacing:.5px">THANK YOU</div>
  <div style="left:56px;top:68px;width:130px;height:1px;background:#d8ccb0"></div>
  <div style="left:0;top:75px;width:242px;text-align:center;font-size:4.4px;font-weight:600;color:var(--white)">KR TMW</div>
  <div style="left:0;top:83px;width:242px;text-align:center;font-size:3.2px;color:var(--white);line-height:1.4">28 Harbor Lane,<br>Westfield, NB 40215</div>
  <div style="left:0;top:96px;width:242px;text-align:center;font-size:3.2px;color:var(--white)">P: 0000 111 222 &nbsp;&bull;&nbsp; www.krtmw-hospitality.com</div>
</section>

</div>
</body>
</html>
```